Business Card Design

RETAIL HIGH END CONTEMPORARY WOMEN'S CLOTHING STORE
MODERN, SIMPLE, CLEAN, COOL

WE ARE ALL ABOUT NY and CALIF STYLE.... CLASSY but EDGY..
COOLEST DENIM , Trendsetting, NEUTRAL Pallettes,
Collections : Thread and Ivy, Corvin Dace, MPW, K47, GVD
Don't need names of collections on card. thats just good info
for designer of card.

WOULD LIKE THE FONT TO BE INTERESTING, but CLEAN
We are on facebook daily with photos of outfits we put together
which you can look up and friend us.... MellowDuneShop
Also on instagram .
Open to options on color and size, but need cool and fresh.

Industry/Entity Type

Business

Contact Information for Business Card

LORNA 5471 Harbor Ave. #318 Cedarline Court Shoppes..Va. Beach, Va. 23987
Phone 757.610.4825 Fax 757.610-3392 EMAIL..LORNABOUTIQUE@MAILVERO.COM

```html
<!DOCTYPE html>
<html lang="en">
<head>
<meta charset="utf-8">
<title>Mellow Dune Shop — Business Card</title>
<link rel="stylesheet" href="https://fonts.googleapis.com/css2?family=Pathway+Gothic+One&display=swap">
<style>
  :root {
    --paper-light: #e3d7c7;
    --paper-mid: #dacbb8;
    --paper-dark: #d2c2ae;
    --vine-tone: #cbb9a3;
    --ink: #4a4038;
    --ink-soft: #5d534b;
    --rule: #8e8378;
  }
  html, body {
    margin: 0;
    padding: 0;
    width: 1200px;
    height: 702px;
    overflow: hidden;
    background: #ffffff;
  }
  .card {
    position: relative;
    width: 1200px;
    height: 702px;
    overflow: hidden;
    font-family: "Pathway Gothic One", "Arial Narrow", sans-serif;
    color: var(--ink);
  }
  .card__pattern {
    position: absolute;
    inset: 0;
    background:
      radial-gradient(ellipse at 20% 30%, var(--vine-tone) 0%, transparent 45%),
      radial-gradient(ellipse at 85% 70%, var(--vine-tone) 0%, transparent 40%),
      linear-gradient(135deg, var(--paper-light) 0%, var(--paper-mid) 55%, var(--paper-dark) 100%);
    opacity: 0.95;
  }
  .card__name {
    position: absolute;
    left: 0;
    right: 0;
    top: 150px;
    margin: 0;
    text-align: center;
    font-family: "Pathway Gothic One", "Arial Narrow", sans-serif;
    font-weight: 400;
    font-size: 128px;
    line-height: 1;
    letter-spacing: 2px;
    color: var(--ink-soft);
  }
  .card__divider {
    position: absolute;
    left: 236px;
    top: 335px;
    width: 728px;
    height: 30px;
  }
  .card__details {
    position: absolute;
    top: 398px;
    margin: 0;
    font-size: 33px;
    line-height: 51px;
    text-align: center;
    font-style: normal;
  }
  .card__address {
    left: 235px;
    width: 300px;
  }
  .card__contact {
    left: 596px;
    width: 450px;
  }
  .card__details span {
    display: block;
  }
</style>
</head>
<body>
  <main class="card">
    <div class="card__pattern" role="img" aria-label="Faint floral vine pattern on warm beige paper"></div>

    <h1 class="card__name">Mellow Dune Shop</h1>

    <svg class="card__divider" viewBox="0 0 728 30" aria-hidden="true">
      <line x1="0" y1="15" x2="326" y2="15" stroke="var(--rule)" stroke-width="1"/>
      <line x1="402" y1="15" x2="728" y2="15" stroke="var(--rule)" stroke-width="1"/>
      <rect x="357" y="4" width="14" height="22" fill="var(--ink-soft)" role="img" aria-label="Small fleuron ornament"/>
    </svg>

    <address class="card__details card__address">
      <span>5471 Harbor Ave. #318</span>
      <span>Cedarline Court Shoppes</span>
      <span>Va. Beach, Va. 23987</span>
    </address>

    <address class="card__details card__contact">
      <span>Phone: 757.610.4825</span>
      <span>Fax: 757.610-3392</span>
      <span>Email: LORNABOUTIQUE@MAILVERO.COM</span>
    </address>
  </main>
</body>
</html>
```